Brovatek a national investment company

We need a logo/letterhead design to describe our business. We use our business across the country to buy and sale property, buy property mineral rights, make investments in small businesses. Our business goal is to promotes integrity, security and growth in small investments. We want our product to reflect our goals.
Updates
I "think" I want a modern, sleek, not too busy design. I "think" I want a dark green and black/grey colors. However, y'all know best and I am looking forward to seeing your creativity in our design. Thanks for accepting our project. -Tobin
We are pleased with some of the designs submitted. We would like for the designs to reflect our company name as it appears on our license, Brovatek. We appreciate the designers who took into consideration our colors we specified. Thanks for all the hard work. We will make a decision tomorrow. You still have time to submit more ideas.
Industry/Entity Type
Investment
Logo Text
Brovatek LLC
Look and feel
Each slider illustrates characteristics of the customer's brand and the style your logo design should communicate.

```html
<!DOCTYPE html>
<html lang="en">
<head>
<meta charset="utf-8">
<title>Brovatek Letterhead</title>
<link rel="stylesheet" href="https://fonts.googleapis.com/css2?family=Open+Sans:wght@400;700&display=swap">
<style>
  :root {
    --backdrop: #ececec;
    --paper: #ffffff;
    --brand-orange: #e8781e;
    --ink-dark: #2b2b2b;
    --ink-grey: #555555;
    --tab-grey: #8a8a8a;
    --watermark: #f7e9dc;
  }
  * { margin: 0; padding: 0; box-sizing: border-box; }
  html, body {
    width: 1200px;
    height: 943px;
    overflow: hidden;
    background: var(--backdrop);
    font-family: "Open Sans", Arial, sans-serif;
  }
  .letterhead {
    position: absolute;
    left: 296px;
    top: 40px;
    width: 608px;
    height: 862px;
    background: var(--paper);
    box-shadow: 0 2px 10px rgba(0,0,0,0.08);
    overflow: hidden;
  }
  .contact-list {
    position: absolute;
    top: 26px;
    right: 40px;
    list-style: none;
    display: flex;
    flex-direction: column;
    gap: 5px;
  }
  .contact-item {
    display: flex;
    align-items: center;
    height: 16px;
  }
  .contact-icon {
    width: 16px;
    height: 16px;
    background: var(--ink-dark);
    display: flex;
    align-items: center;
    justify-content: center;
  }
  .contact-text {
    width: 150px;
    height: 16px;
    background: var(--brand-orange);
    color: var(--paper);
    font-size: 9px;
    line-height: 16px;
    padding-left: 6px;
    white-space: nowrap;
  }
  .contact-tab {
    width: 0;
    height: 0;
    border-top: 8px solid transparent;
    border-bottom: 8px solid transparent;
    border-left: 8px solid var(--tab-grey);
  }
  .brand {
    position: absolute;
    left: 44px;
    top: 168px;
  }
  .brand-name {
    display: flex;
    align-items: center;
    gap: 8px;
    font-size: 30px;
    font-weight: 700;
    color: var(--brand-orange);
    letter-spacing: 0.5px;
    line-height: 1;
  }
  .brand-mark {
    width: 14px;
    height: 14px;
    background: var(--ink-dark);
  }
  .brand-tagline {
    margin-top: 5px;
    font-size: 9.5px;
    color: var(--ink-grey);
  }
  .watermark {
    position: absolute;
    right: -10px;
    bottom: 60px;
    font-size: 112px;
    font-weight: 700;
    color: var(--watermark);
    line-height: 1;
    white-space: nowrap;
  }
</style>
</head>
<body>
  <main class="letterhead">
    <ul class="contact-list">
      <li class="contact-item">
        <span class="contact-icon">
          <svg width="9" height="9" viewBox="0 0 10 10"><path d="M2 1 L4 1 L4.6 3 L3.4 4 Q4.5 6 6 6.6 L7 5.4 L9 6 L9 8 Q8.5 9 7.5 9 Q1 8 1 2.5 Q1 1.5 2 1 Z" fill="#fff"/></svg>
        </span>
        <span class="contact-text">555 014 2288</span>
        <span class="contact-tab"></span>
      </li>
      <li class="contact-item">
        <span class="contact-icon">
          <svg width="9" height="9" viewBox="0 0 10 10"><rect x="1" y="2" width="8" height="6" fill="none" stroke="#fff" stroke-width="1"/><path d="M1 2 L5 5.5 L9 2" fill="none" stroke="#fff" stroke-width="1"/></svg>
        </span>
        <span class="contact-text">mail@brovatek.com</span>
        <span class="contact-tab"></span>
      </li>
      <li class="contact-item">
        <span class="contact-icon">
          <svg width="9" height="9" viewBox="0 0 10 10"><circle cx="5" cy="5" r="4" fill="none" stroke="#fff" stroke-width="1"/><ellipse cx="5" cy="5" rx="1.8" ry="4" fill="none" stroke="#fff" stroke-width="0.8"/><line x1="1" y1="5" x2="9" y2="5" stroke="#fff" stroke-width="0.8"/></svg>
        </span>
        <span class="contact-text">www.brovatek.com</span>
        <span class="contact-tab"></span>
      </li>
      <li class="contact-item">
        <span class="contact-icon">
          <svg width="9" height="9" viewBox="0 0 10 10"><path d="M5 9.5 Q1.5 5.5 1.5 3.6 A3.5 3.5 0 0 1 8.5 3.6 Q8.5 5.5 5 9.5 Z" fill="#fff"/><circle cx="5" cy="3.6" r="1.3" fill="#2b2b2b"/></svg>
        </span>
        <span class="contact-text">12 Alder Road, Dayton</span>
        <span class="contact-tab"></span>
      </li>
    </ul>

    <header class="brand">
      <div class="brand-name"><span class="brand-mark"></span>Brovatek</div>
      <p class="brand-tagline">A National Investment Company</p>
    </header>

    <div class="watermark" aria-hidden="true">Brovatek</div>
  </main>
</body>
</html>
```